QRV Stationery Design Project

Dear Designers,
We need a new stationery design for company to match our new logo.
Designers should provide a design for the following:
1. Business Card: 3.5x2 Inches.
2. Letterhead: A4 size.
3. Envelops: 25x35.5 Cm.
You can keep the Arabic name at the bottom of the logo Or you can use the separate attached Arabic Name.
Please refer to the attached logo guide for design information.
Sample Business Card information:
Name: Tariq Nawaf
Position: Operation Manager
Tel: +966 920007714 Ex. 500
Fax: +966 (3)8842617
Mob: +966 (5)00387251
email: tariq@qrv-example.com.sa
URL: www.qrv-example.com.sa
Address:
Al Wadi Tower, Suite 518
Nasser bin Salem Str.
Jubail, 31847
Saudi Arabia
Updates
Dear All,
Please note, we had uploaded our logo along with Arabic writing in Adobe illustrator format (.ai).
Regards,
Khalid
Dear All,
A sample data for the business card had been added as per your request.
Regards,
Khalid

```html
<!DOCTYPE html>
<html lang="en">
<head>
<meta charset="utf-8">
<title>QRV Letterhead</title>
<link href="https://fonts.googleapis.com/css2?family=Open+Sans:wght@400;700&display=swap" rel="stylesheet">
<style>
  :root {
    --backdrop: #b9b9b9;
    --paper: #ffffff;
    --navy: #1f4a66;
    --steel: #3c6a88;
    --ink: #2c3e4c;
    --link: #2f6f9a;
  }
  * { margin: 0; padding: 0; box-sizing: border-box; }
  html, body {
    width: 1200px;
    height: 900px;
    overflow: hidden;
    background: var(--backdrop);
    font-family: "Open Sans", Arial, sans-serif;
  }
  .letterhead {
    position: absolute;
    left: 303px;
    top: 30px;
    width: 594px;
    height: 840px;
    background: var(--paper);
    box-shadow: 0 4px 18px rgba(0,0,0,0.18);
  }
  .brand {
    position: absolute;
    left: 48px;
    top: 50px;
    display: flex;
    align-items: center;
    gap: 10px;
  }
  .brand-dot {
    width: 22px;
    height: 22px;
    border-radius: 50%;
    background: var(--navy);
  }
  .brand-name {
    font-weight: 700;
    font-size: 40px;
    line-height: 1;
    color: var(--navy);
    letter-spacing: 1px;
  }
  .sender-address {
    position: absolute;
    left: 82px;
    top: 112px;
    font-style: normal;
    font-size: 10px;
    line-height: 1.35;
    color: var(--ink);
  }
  .sender-address .web {
    display: block;
    margin-top: 3px;
    color: var(--link);
  }
  .corner-mark {
    position: absolute;
    right: 0;
    bottom: 0;
    width: 90px;
    height: 90px;
  }
</style>
</head>
<body>
  <main class="letterhead">
    <header class="brand">
      <span class="brand-dot"></span>
      <span class="brand-name">QRV</span>
    </header>
    <address class="sender-address">
      Al Wadi Tower, Suite 518<br>
      Nasser bin Salem Str.<br>
      Jubail, 31847<br>
      Saudi Arabia
      <span class="web">www.qrv-example.com.sa</span>
    </address>
    <svg class="corner-mark" viewBox="0 0 90 90" aria-hidden="true">
      <polygon points="90,0 90,90 0,90" fill="var(--steel)"/>
    </svg>
  </main>
</body>
</html>
```